Engineering Consultant Business Card

I'm starting a new business as a high-end engineering consultant in a niche field. I've attached the jpg for my logo plus the branding guideline document that I've been following. You can see my business website here: www.tarvikworks.com
I'd like a business card that has the logo on one side, then the other side has (in any order): Tarvik Works, Inc.
Dana Whitlock
President and Chief EMC Engineer
www.tarvikworks.com
dana@tarvikworks.com
Optional: motto "We will solve your EMC problems as early as possible—ideally before they even start."
I'm not planning on including a phone number
Target Market(s)
Businesses, especially makers of electronics hardware
Industry/Entity Type
Electrical engineering
Contact Information for Business Card
Company name, my name, website, email

```html
<!DOCTYPE html>
<html lang="en">
<head>
<meta charset="utf-8">
<title>Tarvik Works, Inc. – Business Card</title>
<link href="https://fonts.googleapis.com/css2?family=Inter:wght@400;700&display=swap" rel="stylesheet">
<style>
  :root {
    --stage: #333333;
    --brand-blue: #31479a;
    --pattern-blue: #2f4596;
    --teal: #4fadd0;
    --white: #ffffff;
    --guide: #ffffff;
  }
  * { margin: 0; padding: 0; box-sizing: border-box; }
  html, body {
    width: 1200px; height: 1058px; overflow: hidden;
    background: var(--stage);
    font-family: "Inter", Helvetica, Arial, sans-serif;
  }
  .stage { position: relative; width: 1200px; height: 1058px; }

  .card {
    position: absolute; left: 301px; width: 614px; height: 367px;
    overflow: hidden;
    box-shadow: 0 10px 24px rgba(0,0,0,0.45);
  }
  .card--front { top: 89px; background: var(--brand-blue); }
  .card--back { top: 515px; background: var(--white); }

  .wave-pattern {
    position: absolute; inset: 0;
    background: radial-gradient(circle at 60% 45%, #3550a8 0%, var(--pattern-blue) 70%);
  }

  .wordmark {
    position: absolute; display: flex; align-items: center; gap: 10px;
    color: var(--white); font-weight: 700; white-space: nowrap;
  }
  .wordmark__dot {
    width: 26px; height: 26px; border-radius: 50%;
    border: 4px solid var(--white);
  }
  .card--front .wordmark { left: 47px; top: 108px; font-size: 32px; }

  .motto {
    position: absolute; left: 351px; top: 233px;
    color: var(--white); font-size: 14.5px; line-height: 21.3px;
    text-transform: uppercase; letter-spacing: -0.1px;
  }
  .motto strong { font-weight: 700; }

  .back-band {
    position: absolute; left: 0; top: 0; width: 100%; height: 124px;
    background: var(--brand-blue);
  }
  .card--back .wordmark {
    left: 50%; top: 44px; transform: translateX(-50%); font-size: 32px;
  }

  .holder-name {
    position: absolute; left: 51px; top: 200px;
    color: var(--brand-blue); font-size: 29px; font-weight: 400; letter-spacing: -0.3px;
  }
  .name-rule {
    position: absolute; left: 140px; top: 238px; width: 422px; height: 2px;
    background: var(--brand-blue);
  }
  .holder-title {
    position: absolute; right: 52px; top: 250px;
    color: var(--brand-blue); font-size: 15px;
  }
  .contact-row {
    position: absolute; left: 102px; top: 316px;
    display: flex; align-items: center;
    color: var(--brand-blue); font-size: 16px;
  }
  .contact-row svg { display: block; }
  .contact-item { display: flex; align-items: center; gap: 9px; }
  .contact-divider {
    width: 2px; height: 24px; background: var(--brand-blue); margin: 0 17px 0 17px;
  }
  .accent-bar {
    position: absolute; left: 102px; bottom: 0; width: 411px; height: 14px;
    background: var(--teal);
  }

  .dimension { position: absolute; border-color: var(--guide); border-style: solid; }
  .dimension--height {
    left: 267px; top: 535px; width: 22px; height: 328px;
    border-width: 2px 0 2px 2px;
  }
  .dimension--width {
    left: 320px; top: 896px; width: 577px; height: 27px;
    border-width: 0 2px 2px 2px;
  }
  .dimension-label {
    position: absolute; color: var(--guide); font-size: 26px; white-space: nowrap;
  }
  .dimension-label--height { left: 124px; top: 683px; }
  .dimension-label--width { left: 548px; top: 949px; }
</style>
</head>
<body>
<div class="stage">

  <section class="card card--front">
    <div class="wave-pattern" role="img" aria-label="Decorative pattern of overlapping concentric wave rings in tonal blue"></div>
    <div class="wordmark"><span class="wordmark__dot"></span>Tarvik Works</div>
    <p class="motto">
      We will solve your<br>
      <strong>EMC</strong> problems as<br>
      early as possible—ideally<br>
      before they even start
    </p>
  </section>

  <section class="card card--back">
    <div class="back-band"></div>
    <div class="wordmark"><span class="wordmark__dot"></span>Tarvik Works</div>

    <h1 class="holder-name">Dana Whitlock</h1>
    <div class="name-rule"></div>
    <p class="holder-title">President and Chief EMC Engineer</p>

    <div class="contact-row">
      <span class="contact-item">
        <svg width="16" height="12" viewBox="0 0 16 12" aria-hidden="true">
          <rect x="0" y="0" width="16" height="12" rx="1" fill="#31479a"/>
          <path d="M1 1.5 L8 7 L15 1.5" fill="none" stroke="#ffffff" stroke-width="1.4"/>
        </svg>
        dana@tarvikworks.com
      </span>
      <span class="contact-divider"></span>
      <span class="contact-item">
        <svg width="14" height="14" viewBox="0 0 14 14" aria-hidden="true">
          <circle cx="7" cy="7" r="6" fill="none" stroke="#31479a" stroke-width="1.6"/>
          <ellipse cx="7" cy="7" rx="2.6" ry="6" fill="none" stroke="#31479a" stroke-width="1.4"/>
          <line x1="1" y1="7" x2="13" y2="7" stroke="#31479a" stroke-width="1.4"/>
        </svg>
        www.tarvikworks.com
      </span>
    </div>
    <div class="accent-bar"></div>
  </section>

  <div class="dimension dimension--height"></div>
  <span class="dimension-label dimension-label--height">2 inches</span>
  <div class="dimension dimension--width"></div>
  <span class="dimension-label dimension-label--width">3.5 inches</span>

</div>
</body>
</html>
```